Crestmoor Air Global Business Card

I would like a professional business card designed. The plane that is being used is a Skyvane Aero Marshal 2400. Our primary business colors would be navy blue and light blue. This is a charter plane for hire. Our clients range from business people to vacation goers. A website is currently under development and two of the primary pictures being used will be attached. The pictures don't need to be used in the business card design, but could be used for inspiration and reference. We will need our P.O. Box address on the card and personal information (Name, cell number, email address, and website address (www.crestmoorairglobal.example)) Thanks! God Bless!
Updates

The contact info for the back of the card: Dale Whitcombe Cell: 555.014.2867 Email: dwhitcombe@crestmoorairglobal.example

Target Market(s)

Business people

Industry/Entity Type

Business

Contact Information for Business Card

This will be on a standard square cornered business card.

Requirements
Must have
• Professional look

```html
<!DOCTYPE html>
<html lang="en">
<head>
<meta charset="utf-8">
<title>Crestmoor Air Global Business Card</title>
<link rel="stylesheet" href="https://fonts.googleapis.com/css2?family=Open+Sans:wght@400;600;700&display=swap">
<style>
  :root {
    --page-bg: #d9d9d9;
    --card-bg: #0c0c0d;
    --card-bg-edge: #141416;
    --brand-blue: #2f47b3;
    --text-light: #f4f4f4;
    --rule: #2a2a2e;
  }
  * { box-sizing: border-box; margin: 0; padding: 0; }
  html, body {
    width: 1200px; height: 900px; overflow: hidden;
    background: var(--page-bg);
    font-family: "Open Sans", Arial, sans-serif;
  }
  .sheet {
    position: relative; width: 1200px; height: 900px;
    display: flex; flex-direction: column; align-items: center; justify-content: center; gap: 36px;
  }
  .card {
    position: relative; width: 700px; height: 400px;
    background: linear-gradient(135deg, var(--card-bg-edge), var(--card-bg) 60%);
    box-shadow: 0 6px 18px rgba(0,0,0,0.25);
    overflow: hidden;
  }
  .brand {
    display: flex; align-items: center; gap: 14px;
    color: var(--brand-blue); font-weight: 700; text-transform: uppercase;
    letter-spacing: 0.02em; white-space: nowrap;
  }
  .brand-dot { flex: none; border-radius: 50%; background: var(--brand-blue); }
  /* front */
  .card-front { display: flex; align-items: center; justify-content: center; }
  .card-front .brand { font-size: 40px; }
  .card-front .brand-dot { width: 30px; height: 30px; }
  /* back */
  .card-back .brand {
    position: absolute; top: 96px; right: 56px; font-size: 25px; gap: 10px;
  }
  .card-back .brand-dot { width: 18px; height: 18px; }
  .holder { position: absolute; left: 46px; top: 112px; }
  .holder-name { color: var(--text-light); font-size: 26px; font-weight: 600; line-height: 1.1; }
  .holder-title { color: var(--brand-blue); font-size: 16px; margin-top: 4px; }
  .divider {
    position: absolute; left: 230px; right: 56px; top: 178px;
    height: 1px; background: var(--rule);
  }
  .contact-list {
    position: absolute; right: 40px; bottom: 34px; list-style: none;
    display: flex; flex-direction: column; align-items: flex-end; gap: 3px;
  }
  .contact-item {
    display: flex; align-items: center; gap: 12px;
    color: var(--text-light); font-size: 17px; line-height: 1.3; white-space: nowrap;
  }
  .contact-icon { flex: none; width: 14px; height: 14px; fill: none; stroke: var(--brand-blue); stroke-width: 1.8; }
  .contact-icon .solid { fill: var(--brand-blue); stroke: none; }
</style>
</head>
<body>
<main class="sheet">
  <section class="card card-front" aria-label="Card front">
    <div class="brand"><span class="brand-dot"></span>Crestmoor Air Global</div>
  </section>

  <section class="card card-back" aria-label="Card back">
    <div class="holder">
      <p class="holder-name">Dale Whitcombe</p>
      <p class="holder-title">Managing Director</p>
    </div>
    <div class="brand"><span class="brand-dot"></span>Crestmoor Air Global</div>
    <div class="divider"></div>
    <ul class="contact-list">
      <li class="contact-item">555.014.2867
        <svg class="contact-icon" viewBox="0 0 14 14" aria-hidden="true"><rect x="3.5" y="1" width="7" height="12" rx="1.2"/><circle class="solid" cx="7" cy="10.8" r="0.9"/></svg>
      </li>
      <li class="contact-item">555.014.3190
        <svg class="contact-icon" viewBox="0 0 14 14" aria-hidden="true"><path class="solid" d="M1 5c0-2 2-3 6-3s6 1 6 3v1h-3V4.5H4V6H1z"/><rect class="solid" x="2.5" y="7" width="9" height="5.5" rx="1"/></svg>
      </li>
      <li class="contact-item">dwhitcombe@crestmoorairglobal.example
        <svg class="contact-icon" viewBox="0 0 14 14" aria-hidden="true"><rect x="1" y="3" width="12" height="8.5" rx="1"/><path d="M1.5 3.5 7 8l5.5-4.5"/></svg>
      </li>
      <li class="contact-item">www.crestmoorairglobal.example
        <svg class="contact-icon" viewBox="0 0 14 14" aria-hidden="true"><path d="M6 8.5 8.5 6M5 6.5 3.2 8.3a2 2 0 0 0 2.8 2.8L7.8 9.3M9 7.5l1.8-1.8A2 2 0 0 0 8 2.9L6.2 4.7"/></svg>
      </li>
      <li class="contact-item">P.O. Box 1482, Ashford Springs, CO 80000
        <svg class="contact-icon" viewBox="0 0 14 14" aria-hidden="true"><path d="M7 13s4.5-4.2 4.5-7.5a4.5 4.5 0 0 0-9 0C2.5 8.8 7 13 7 13z"/><circle class="solid" cx="7" cy="5.5" r="1.5"/></svg>
      </li>
    </ul>
  </section>
</main>
</body>
</html>
```